Electrical Engineering Business Card Design

I need a business card design for an engineering consulting company based in Orlando, FL. I have had a logo created which the files are attached. We work primarily in the theme park and entertainment market sector but do projects in all market sectors. We have been serving Central Florida since 1994 and continue to strive to serve our clients and provide outstanding designs.
Theme Park

```html
<!DOCTYPE html>
<html lang="en">
<head>
<meta charset="utf-8">
<title>Brightwell Associates, P.A. – Business Card</title>
<link rel="stylesheet" href="https://fonts.googleapis.com/css2?family=Oswald:wght@600&family=Poppins:wght@400;500&display=swap">
<style>
  :root {
    --backdrop: #e6e3dc;
    --card: #ffffff;
    --card-shade: #f1f1f1;
    --green: #8cc63f;
    --green-light: #a6d65e;
    --ink: #2b2b2b;
    --ink-soft: #3c3c3c;
  }
  * { margin: 0; padding: 0; box-sizing: border-box; }
  html, body {
    width: 1200px; height: 800px; overflow: hidden;
    background: var(--backdrop);
  }
  .canvas {
    width: 1200px; height: 800px;
    display: flex; flex-direction: column;
    align-items: center; justify-content: center; gap: 36px;
  }
  .card {
    position: relative;
    width: 630px; height: 360px;
    background: linear-gradient(160deg, var(--card) 40%, var(--card-shade));
    box-shadow: 0 6px 18px rgba(0,0,0,.18);
    overflow: hidden;
  }
  .card__band {
    position: absolute; left: 0; right: 0; height: 22px;
    background: var(--green);
  }
  .card__band--top { top: 0; background: linear-gradient(var(--green-light), var(--green)); }
  .card__band--bottom { bottom: 0; }

  .lockup {
    position: absolute; left: 0; right: 0;
    display: flex; flex-direction: column; align-items: center;
  }
  .card--front .lockup { top: 92px; }
  .card--back .lockup { top: 62px; }
  .lockup__mark {
    width: 46px; height: 46px; background: var(--green);
    margin-bottom: 14px;
  }
  .lockup__name {
    font-family: "Oswald", sans-serif; font-weight: 600;
    font-size: 38px; line-height: 1; color: var(--ink);
    letter-spacing: .5px;
  }
  .lockup__place {
    font-family: "Poppins", sans-serif; font-weight: 500;
    font-size: 14px; letter-spacing: 5px; color: var(--ink);
    margin-top: 6px;
  }

  .contacts {
    position: absolute; left: 30px; right: 30px; bottom: 48px;
    display: flex; justify-content: space-between; align-items: center;
    list-style: none;
  }
  .contact {
    display: flex; align-items: center; gap: 9px;
    font-family: "Poppins", sans-serif; font-size: 11px; line-height: 1.35;
    color: var(--ink-soft);
  }
  .contact__icon {
    width: 22px; height: 22px; flex: none;
    border: 1.5px solid var(--green);
    display: flex; align-items: center; justify-content: center;
  }
  .contact__icon svg { width: 12px; height: 12px; }
</style>
</head>
<body>
<main class="canvas">

  <section class="card card--front" aria-label="Card front">
    <div class="card__band card__band--top"></div>
    <div class="lockup">
      <div class="lockup__mark"></div>
      <h1 class="lockup__name">Brightwell Associates, P.A.</h1>
      <p class="lockup__place">ORLANDO, FLORIDA</p>
    </div>
    <div class="card__band card__band--bottom"></div>
  </section>

  <section class="card card--back" aria-label="Card back">
    <div class="card__band card__band--top"></div>
    <div class="lockup">
      <div class="lockup__mark"></div>
      <h2 class="lockup__name">Brightwell Associates, P.A.</h2>
      <p class="lockup__place">ORLANDO, FLORIDA</p>
    </div>
    <ul class="contacts">
      <li class="contact">
        <span class="contact__icon">
          <svg viewBox="0 0 12 12"><path d="M6 1a3.3 3.3 0 0 0-3.3 3.3C2.7 7 6 11 6 11s3.3-4 3.3-6.7A3.3 3.3 0 0 0 6 1z" fill="var(--green)"/><circle cx="6" cy="4.3" r="1.2" fill="#fff"/></svg>
        </span>
        <span>PO Box 100234<br>Orlando, FL 32801</span>
      </li>
      <li class="contact">
        <span class="contact__icon">
          <svg viewBox="0 0 12 12"><rect x="1" y="2.5" width="10" height="7" fill="none" stroke="var(--green)" stroke-width="1.3"/><path d="M1 2.5l5 4 5-4" fill="none" stroke="var(--green)" stroke-width="1.3"/></svg>
        </span>
        <span>office@brightwellpa.com</span>
      </li>
      <li class="contact">
        <span class="contact__icon">
          <svg viewBox="0 0 12 12"><path d="M3 1l2 2.5-1.2 1.3a7 7 0 0 0 3.4 3.4L8.5 7 11 9l-1.3 1.8C6 11 1 6 1.2 2.3z" fill="var(--green)"/></svg>
        </span>
        <span>407-555-0142</span>
      </li>
      <li class="contact">
        <span class="contact__icon">
          <svg viewBox="0 0 12 12"><rect x="3" y="1" width="6" height="3" fill="none" stroke="var(--green)" stroke-width="1.2"/><rect x="1" y="4" width="10" height="5" fill="var(--green)"/><rect x="3" y="7.5" width="6" height="3.5" fill="#fff" stroke="var(--green)" stroke-width="1.2"/></svg>
        </span>
        <span>407-555-0178</span>
      </li>
    </ul>
    <div class="card__band card__band--bottom"></div>
  </section>

</main>
</body>
</html>
```